Uprising SaaS company needs an attractive business card design

We're an uprising SaaS company who's attempting to attack the rigid car (insurance) claims management market in Europe.
We want to our mighty base order management system, listen to our clients to connect the smart ideas to build something even mightier.
We primarily focus on helping our customers manage their customers' claims/orders and get them resolved as smoothly as possible.
We'd like the business card design to express technical innovation and the fact that we connect smart ideas, as our company slogan indicates.
Contact Information for Business Card
Name, position, website, email, mobile, business address
Font styles to use
Colors
Designer to choose colors to be used in the design.
Look and feel
Each slider illustrates characteristics of the customer's brand and the style your logo design should communicate.

```html
<!DOCTYPE html>
<html lang="en">
<head>
<meta charset="utf-8">
<title>nervora business card</title>
<link rel="stylesheet" href="https://fonts.googleapis.com/css2?family=Montserrat:wght@700&family=Raleway:wght@300;400&display=swap">
<style>
  :root {
    --backdrop: #6a7668;
    --card-dark: #000000;
    --card-light: #ffffff;
    --brand-grey: #8a8a8a;
    --brand-sky: #86d3ea;
    --ink: #3a3a3a;
    --rule: #444444;
  }
  * { margin: 0; padding: 0; box-sizing: border-box; }
  html, body { width: 1200px; height: 920px; overflow: hidden; }
  body {
    background: var(--backdrop);
    position: relative;
    font-family: "Raleway", sans-serif;
  }
  .card {
    position: absolute;
    left: 320px;
    width: 560px;
    height: 320px;
    box-shadow: 0 18px 40px rgba(0,0,0,0.35);
  }
  .card--front {
    top: 110px;
    background: var(--card-dark);
    display: flex;
    align-items: center;
    justify-content: center;
  }
  .card--back {
    top: 490px;
    background: var(--card-light);
  }
  .wordmark {
    font-family: "Raleway", sans-serif;
    font-weight: 300;
    color: var(--brand-sky);
    letter-spacing: 2px;
    line-height: 1;
  }
  .card--front .wordmark { font-size: 96px; }
  .card--back .wordmark {
    position: absolute;
    top: 44px;
    right: 40px;
    font-size: 40px;
  }
  .holder {
    position: absolute;
    left: 40px;
    top: 150px;
  }
  .holder__name {
    font-family: "Montserrat", sans-serif;
    font-weight: 700;
    font-size: 24px;
    color: var(--brand-grey);
    letter-spacing: -0.5px;
  }
  .holder__role {
    font-size: 15px;
    color: var(--ink);
    margin-top: 2px;
  }
  .divider {
    position: absolute;
    left: 40px;
    top: 202px;
    width: 160px;
    height: 1px;
    background: var(--rule);
  }
  .divider--long {
    left: 210px;
    top: 150px;
    width: 310px;
  }
  .address {
    position: absolute;
    right: 40px;
    top: 166px;
    text-align: right;
    font-size: 15px;
    line-height: 1.45;
    color: var(--ink);
  }
  .contacts {
    position: absolute;
    left: 40px;
    top: 214px;
    list-style: none;
  }
  .contacts__item {
    display: flex;
    align-items: center;
    gap: 10px;
    font-size: 14px;
    color: var(--ink);
    height: 26px;
  }
  .contacts__icon { width: 14px; height: 14px; flex: none; }
</style>
</head>
<body>
  <section class="card card--front">
    <span class="wordmark">nervora</span>
  </section>

  <section class="card card--back">
    <span class="wordmark">nervora</span>

    <div class="divider divider--long"></div>
    <address class="address">88, Harbour Lane West<br>Rotterdam, 30112</address>

    <div class="holder">
      <h1 class="holder__name">MARCUS HALE</h1>
      <p class="holder__role">Managing Director</p>
    </div>

    <div class="divider"></div>

    <ul class="contacts">
      <li class="contacts__item">
        <svg class="contacts__icon" viewBox="0 0 24 24" aria-hidden="true">
          <path fill="var(--brand-sky)" d="M6.6 10.8a15.2 15.2 0 0 0 6.6 6.6l2.2-2.2c.3-.3.7-.4 1-.2 1.1.4 2.3.6 3.6.6.6 0 1 .4 1 1V20c0 .6-.4 1-1 1A17 17 0 0 1 3 4c0-.6.4-1 1-1h3.5c.6 0 1 .4 1 1 0 1.3.2 2.5.6 3.6.1.3 0 .7-.2 1z"/>
        </svg>
        044-987 650 312
      </li>
      <li class="contacts__item">
        <svg class="contacts__icon" viewBox="0 0 24 24" aria-hidden="true">
          <rect x="2" y="5" width="20" height="14" rx="1" fill="var(--brand-sky)"/>
          <path d="M2 6l10 7 10-7" fill="none" stroke="#ffffff" stroke-width="1.6"/>
        </svg>
        hello@nervora.eu
      </li>
      <li class="contacts__item">
        <svg class="contacts__icon" viewBox="0 0 24 24" aria-hidden="true">
          <circle cx="12" cy="12" r="10" fill="var(--brand-sky)"/>
          <path d="M2 12h20M12 2c3 3 3 17 0 20M12 2c-3 3-3 17 0 20" fill="none" stroke="#ffffff" stroke-width="1.4"/>
        </svg>
        www.nervora.eu
      </li>
    </ul>
  </section>
</body>
</html>
```